Corvane Holdings , new business card design

investment firm with corporate clients . need double sided business card , vertical and horizontal options ,logo must be clear. prefer pantone colors only and sharp design. website also www.corvane-example.ae

Khalid Bin Rashed
Managing Director
Tel. +971 4 000 3829
Mobile +971 50 000 4172
khalid@corvane-example.ae
Palm Crest Tower, officw 18-B07, Qasr Gardens, Dubai

Contact Information for Business Card

Khalid Bin Rashed
Managing Director

Font styles to use
Serif

Colors

Designer to choose colors to be used in the design.

```html
<!DOCTYPE html>
<html lang="en">
<head>
<meta charset="utf-8">
<title>Corvane Holdings – Business Card</title>
<link href="https://fonts.googleapis.com/css2?family=EB+Garamond:wght@400;500&display=swap" rel="stylesheet">
<style>
  :root {
    --backdrop: #838488;
    --card: #ffffff;
    --brand-blue: #3f6b9a;
    --text-grey: #7d7d7f;
    --ink: #1b1b1d;
  }
  * { margin: 0; padding: 0; box-sizing: border-box; }
  html, body {
    width: 1052px;
    height: 1200px;
    overflow: hidden;
    background: var(--backdrop);
    font-family: "EB Garamond", Garamond, serif;
  }
  .canvas {
    position: relative;
    width: 1052px;
    height: 1200px;
  }
  .card {
    position: absolute;
    left: 246px;
    width: 564px;
    height: 326px;
    background: var(--card);
  }
  .card--front { top: 232px; }
  .card--back  { top: 648px; }

  .holder-name {
    position: absolute;
    left: 299px;
    top: 288px;
    color: var(--brand-blue);
    font-size: 20px;
    letter-spacing: 0.3px;
    text-transform: uppercase;
  }
  .holder-role {
    position: absolute;
    left: 299px;
    top: 313px;
    color: var(--text-grey);
    font-size: 19px;
  }
  .contact-list {
    position: absolute;
    left: 298px;
    top: 364px;
    list-style: none;
  }
  .contact-item {
    display: flex;
    align-items: center;
    height: 29px;
    color: var(--text-grey);
    font-size: 19px;
  }
  .contact-icon {
    width: 22px;
    height: 22px;
    margin-right: 8px;
    flex: none;
  }
  .website {
    position: absolute;
    left: 0;
    right: 0;
    top: 498px;
    text-align: center;
    color: var(--brand-blue);
    font-size: 20px;
    letter-spacing: 3px;
  }
  .brand-name {
    position: absolute;
    left: 0;
    right: 0;
    top: 146px;
    padding-left: 5px;
    text-align: center;
    color: var(--ink);
    font-size: 25px;
    font-weight: 400;
    letter-spacing: 5px;
    line-height: 1;
    text-transform: uppercase;
    white-space: nowrap;
  }
</style>
</head>
<body>
<main class="canvas">
  <section class="card card--front" aria-label="Card front"></section>
  <p class="holder-name">Khalid Bin Rashed</p>
  <p class="holder-role">Managing Director</p>
  <ul class="contact-list">
    <li class="contact-item">
      <svg class="contact-icon" viewBox="0 0 22 22" aria-hidden="true">
        <circle cx="11" cy="11" r="10" fill="none" stroke="#7d7d7f" stroke-width="1.2"/>
        <path d="M7.5 6.5l2 0 1 2.5-1.3 1c.6 1.3 1.5 2.2 2.8 2.8l1-1.3 2.5 1v2c-4.5.3-8.3-3.5-8-8z" fill="none" stroke="#7d7d7f" stroke-width="1.1" stroke-linejoin="round"/>
      </svg>+971 4 000 3829</li>
    <li class="contact-item">
      <svg class="contact-icon" viewBox="0 0 22 22" aria-hidden="true">
        <circle cx="11" cy="11" r="10" fill="none" stroke="#7d7d7f" stroke-width="1.2"/>
        <rect x="8" y="5.5" width="6" height="11" rx="1" fill="none" stroke="#7d7d7f" stroke-width="1.1"/>
        <line x1="10" y1="14.5" x2="12" y2="14.5" stroke="#7d7d7f" stroke-width="1"/>
      </svg>+971 50 000 4172</li>
    <li class="contact-item">
      <svg class="contact-icon" viewBox="0 0 22 22" aria-hidden="true">
        <circle cx="11" cy="11" r="10" fill="none" stroke="#7d7d7f" stroke-width="1.2"/>
        <rect x="6" y="7.5" width="10" height="7" fill="#7d7d7f"/>
        <path d="M6 7.5l5 4 5-4" fill="none" stroke="#ffffff" stroke-width="1"/>
      </svg>khalid@corvane-example.ae</li>
    <li class="contact-item">
      <svg class="contact-icon" viewBox="0 0 22 22" aria-hidden="true">
        <circle cx="11" cy="11" r="10" fill="none" stroke="#7d7d7f" stroke-width="1.2"/>
        <path d="M11 17s-4-4.3-4-7a4 4 0 0 1 8 0c0 2.7-4 7-4 7z" fill="#7d7d7f"/>
        <circle cx="11" cy="10" r="1.5" fill="#ffffff"/>
      </svg>Palm Crest Tower, officw 18-B07, Qasr Gardens, Dubai</li>
  </ul>
  <p class="website">www.corvane-example.ae</p>

  <section class="card card--back" aria-label="Card back">
    <p class="brand-name">Corvane Holdings</p>
  </section>
</main>
</body>
</html>
```